TALLVEX MOTOR OIL LABEL

I am launching a new motor oil product called TallVex and I would like your help in designing the packaging. The product is aimed at delivering high-performance results for vehicles, and I want the packaging to reflect the premium quality and reliability of TallVex. The design should be modern, dynamic, and appeal to car enthusiasts, while also communicating trust and innovation. I’m looking for a sleek and professional look that stands out on the shelf. Please incorporate elements that highlight its efficiency and performance, with bold typography and striking colors to grab attention.
I also need a logo for the name TallVex, and I would like your help in choosing the right colors for the packaging. The logo should be bold, memorable, and represent the strength and high performance of the product. When it comes to the packaging colors, I want something that is both eye-catching and conveys a sense of power and reliability, while also appealing to car enthusiasts. Your guidance in selecting the perfect color scheme to match the brand identity will be greatly appreciated.
The types of oils I plan to offer are available in the following sizes: 1 liter, 4 liters, and 5 liters.

• 10W40 Synthetic Blend High Mileage
• 20W50 Synthetic Blend High Mileage
• 10W30 Synthetic Blend High Mileage
• 5W30 Synthetic Blend High Mileage
• 5W20 Synthetic Blend High Mileage

Additionally, I will offer

Additionally, I will offer a
0W16 FULL SYNTHETIC
OW20 FULL SYNTHETIC
5W20 FULL SYNTHETIC
5W30 FULL SYNTHETIC
5W40 FULL SYNTHETIC
0W40 FULL SYNTHETIC
AND HD MOTOR OIL
15W40 HAVEY DUTY DIESEL ENGINE OIL SYNTHETIC BLEND
5W40 HAVEY DUTY DIESEL ENGINE OIL FULL SYNTHETIC

Font styles to use
Serif

Colors
0054AA
0677BA
7BADD7
CADEEF
E8F1F8
59FF00
82FF00
B8FF75
E3FFCB
F4FFEA
FFF300
FFF600
FEFA6F
FFFEC7
FFFEE8
FFC000
F8CF3A
FAE287
FDF2CF
FEFAEE
F0912C
F2A743
F7CA91
FBE8D2
FDF5EE
EB3D1F
EC4F4E
F09395
F8D3D4
FCEDEE

```html
<!DOCTYPE html>
<html lang="en">
<head>
<meta charset="utf-8">
<title>TallVex 5W30 Label Set</title>
<link rel="stylesheet" href="https://fonts.googleapis.com/css2?family=Barlow+Condensed:ital,wght@0,600;0,700;1,600;1,700&family=Montserrat:wght@400;500;700&display=swap">
<style>
  :root {
    --ink: #1c1c1a;
    --yellow: #fff300;
    --white: #ffffff;
    --caption: #1a1a1a;
  }
  * { box-sizing: border-box; margin: 0; padding: 0; }
  html, body { width: 1200px; height: 804px; overflow: hidden; background: var(--white); }
  .sheet { position: relative; width: 1200px; height: 804px; }

  .variant { position: absolute; top: 110px; width: 340px; }
  .variant--one { left: 60px; }
  .variant--five { left: 430px; }
  .variant--four { left: 800px; }

  .label {
    position: relative; width: 340px; height: 485px; overflow: hidden;
    clip-path: polygon(0 80px, 100% 0, 100% 100%, 0 100%);
    color: var(--white);
  }
  .label__art { position: absolute; inset: 0; width: 100%; height: 100%; }

  .brand {
    position: absolute; left: 24px; top: 108px;
    transform: rotate(-13deg); transform-origin: left top;
  }
  .brand__name {
    font-family: "Barlow Condensed", sans-serif; font-weight: 700;
    font-size: 54px; line-height: 0.9; letter-spacing: 0.5px; color: var(--white);
  }
  .brand__tagline {
    display: inline-block; margin-top: 3px; padding: 1px 6px;
    background: var(--yellow); color: var(--ink);
    font-family: "Barlow Condensed", sans-serif; font-weight: 700;
    font-size: 8.5px; letter-spacing: 2.4px;
  }

  .grade {
    position: absolute; left: 138px; top: 214px; width: 186px;
    transform: rotate(-6deg); transform-origin: left top;
  }
  .grade__viscosity {
    font-family: "Montserrat", sans-serif; font-weight: 700;
    font-size: 56px; line-height: 1; letter-spacing: 1px; text-align: right;
  }
  .grade__type {
    display: inline-block; margin-top: 2px; padding: 0 8px;
    background: var(--yellow); color: var(--ink);
    font-family: "Barlow Condensed", sans-serif; font-style: italic; font-weight: 600;
    font-size: 24px; line-height: 1.15;
  }
  .grade__line {
    font-family: "Barlow Condensed", sans-serif; font-style: italic; font-weight: 700;
    font-size: 36px; line-height: 1.05;
  }

  .features {
    position: absolute; left: 140px; top: 378px; width: 180px;
    display: grid; grid-template-columns: 1fr 1fr; row-gap: 8px; column-gap: 6px;
    font-family: "Barlow Condensed", sans-serif; font-weight: 600; font-size: 9px; letter-spacing: 0.3px;
  }
  .feature { display: flex; align-items: center; gap: 5px; }
  .feature svg { width: 12px; height: 12px; flex: none; }

  .blurb {
    position: absolute; left: 120px; top: 432px; width: 140px;
    font-family: "Montserrat", sans-serif; font-weight: 500; font-size: 6.6px; line-height: 1.2;
    text-align: right; color: var(--ink);
  }
  .seal { position: absolute; left: 266px; top: 424px; width: 44px; height: 44px; }

  .volume { position: absolute; left: 16px; top: 424px; display: flex; align-items: center; gap: 3px; }
  .volume__number {
    font-family: "Barlow Condensed", sans-serif; font-weight: 700; font-size: 38px; line-height: 1;
  }
  .volume__unit {
    writing-mode: vertical-rl; transform: rotate(180deg);
    background: var(--yellow); color: var(--ink);
    font-family: "Barlow Condensed", sans-serif; font-weight: 700; font-size: 6px; letter-spacing: 0.8px;
    padding: 1px 0;
  }

  .variant__caption {
    margin-top: 32px; text-align: center;
    font-family: "Montserrat", sans-serif; font-weight: 400; font-size: 30px; color: var(--caption);
  }
</style>
</head>
<body>
<main class="sheet">

  <svg width="0" height="0" style="position:absolute" aria-hidden="true">
    <defs>
      <linearGradient id="label-base" x1="0" y1="0" x2="1" y2="1">
        <stop offset="0" stop-color="#1f1f1d"/>
        <stop offset="0.4" stop-color="#34332a"/>
        <stop offset="0.62" stop-color="#5a5840"/>
        <stop offset="0.8" stop-color="#6a6820"/>
        <stop offset="1" stop-color="#f2ea2a"/>
      </linearGradient>
      <symbol id="label-art" viewBox="0 0 340 485">
        <rect width="340" height="485" fill="url(#label-base)"/>
        <line x1="128" y1="354" x2="340" y2="338" stroke="#f2ea2a" stroke-width="1.5"/>
      </symbol>
      <symbol id="icon-gauge" viewBox="0 0 12 12">
        <circle cx="6" cy="6" r="5" fill="none" stroke="#fff" stroke-width="1.2"/>
        <line x1="6" y1="6" x2="9" y2="3.5" stroke="#fff" stroke-width="1.2"/>
      </symbol>
      <symbol id="icon-engine" viewBox="0 0 12 12">
        <rect x="2" y="3" width="8" height="6" rx="1" fill="#fff"/>
        <rect x="0.5" y="5" width="1.5" height="2" fill="#fff"/>
        <rect x="10" y="5" width="1.5" height="2" fill="#fff"/>
      </symbol>
      <symbol id="icon-clock" viewBox="0 0 12 12">
        <circle cx="6" cy="6" r="5" fill="none" stroke="#fff" stroke-width="1.2"/>
        <path d="M6 3 V6 H8.5" fill="none" stroke="#fff" stroke-width="1.2"/>
      </symbol>
      <symbol id="icon-gear" viewBox="0 0 12 12">
        <circle cx="6" cy="6" r="4" fill="none" stroke="#fff" stroke-width="2.4" stroke-dasharray="2 1.2"/>
        <circle cx="6" cy="6" r="1.5" fill="#fff"/>
      </symbol>
      <symbol id="seal" viewBox="0 0 44 44">
        <circle cx="22" cy="22" r="21" fill="#1a1a1a"/>
        <circle cx="22" cy="22" r="15" fill="#ffffff"/>
        <circle cx="22" cy="22" r="11" fill="#eb3d1f"/>
      </symbol>
    </defs>
  </svg>

  <section class="variant variant--one">
    <div class="label">
      <svg class="label__art" viewBox="0 0 340 485" preserveAspectRatio="none" role="img" aria-label="Label backdrop: pinstripe texture and silver swoosh over a charcoal-to-yellow gradient"><use href="#label-art"/></svg>
      <div class="brand"><div class="brand__name">TALLVEX</div><span class="brand__tagline">HIGH PERFOMANCE MOTOR OIL</span></div>
      <div class="grade">
        <div class="grade__viscosity">5W30</div>
        <span class="grade__type">SYNTHETIC BLEND</span>
        <div class="grade__line">HIGH MILEAGE</div>
      </div>
      <div class="features">
        <div class="feature"><svg><use href="#icon-gauge"/></svg>HIGH PERFOMANCE</div>
        <div class="feature"><svg><use href="#icon-engine"/></svg>BOOSTS ENGINE</div>
        <div class="feature"><svg><use href="#icon-clock"/></svg>LONG-LASTING</div>
        <div class="feature"><svg><use href="#icon-gear"/></svg>HIGH EFFICIENCY</div>
      </div>
      <p class="blurb">Engineered for excellence, TallVex delivers unmatched protection and efficiency, keeping your engine running smoother for longer.</p>
      <svg class="seal" viewBox="0 0 44 44" role="img" aria-label="Engine certification seal"><use href="#seal"/></svg>
      <div class="volume"><span class="volume__number">1</span><span class="volume__unit">QUART</span></div>
    </div>
    <p class="variant__caption">1 Quarts</p>
  </section>

  <section class="variant variant--five">
    <div class="label">
      <svg class="label__art" viewBox="0 0 340 485" preserveAspectRatio="none" role="img" aria-label="Label backdrop: pinstripe texture and silver swoosh over a charcoal-to-yellow gradient"><use href="#label-art"/></svg>
      <div class="brand"><div class="brand__name">TALLVEX</div><span class="brand__tagline">HIGH PERFOMANCE MOTOR OIL</span></div>
      <div class="grade">
        <div class="grade__viscosity">5W30</div>
        <span class="grade__type">SYNTHETIC BLEND</span>
        <div class="grade__line">HIGH MILEAGE</div>
      </div>
      <div class="features">
        <div class="feature"><svg><use href="#icon-gauge"/></svg>HIGH PERFOMANCE</div>
        <div class="feature"><svg><use href="#icon-engine"/></svg>BOOSTS ENGINE</div>
        <div class="feature"><svg><use href="#icon-clock"/></svg>LONG-LASTING</div>
        <div class="feature"><svg><use href="#icon-gear"/></svg>HIGH EFFICIENCY</div>
      </div>
      <p class="blurb">Engineered for excellence, TallVex delivers unmatched protection and efficiency, keeping your engine running smoother for longer.</p>
      <svg class="seal" viewBox="0 0 44 44" role="img" aria-label="Engine certification seal"><use href="#seal"/></svg>
      <div class="volume"><span class="volume__number">5</span><span class="volume__unit">QUARTS</span></div>
    </div>
    <p class="variant__caption">5 Quarts</p>
  </section>

  <section class="variant variant--four">
    <div class="label">
      <svg class="label__art" viewBox="0 0 340 485" preserveAspectRatio="none" role="img" aria-label="Label backdrop: pinstripe texture and silver swoosh over a charcoal-to-yellow gradient"><use href="#label-art"/></svg>
      <div class="brand"><div class="brand__name">TALLVEX</div><span class="brand__tagline">HIGH PERFOMANCE MOTOR OIL</span></div>
      <div class="grade">
        <div class="grade__viscosity">5W30</div>
        <span class="grade__type">SYNTHETIC BLEND</span>
        <div class="grade__line">HIGH MILEAGE</div>
      </div>
      <div class="features">
        <div class="feature"><svg><use href="#icon-gauge"/></svg>HIGH PERFOMANCE</div>
        <div class="feature"><svg><use href="#icon-engine"/></svg>BOOSTS ENGINE</div>
        <div class="feature"><svg><use href="#icon-clock"/></svg>LONG-LASTING</div>
        <div class="feature"><svg><use href="#icon-gear"/></svg>HIGH EFFICIENCY</div>
      </div>
      <p class="blurb">Engineered for excellence, TallVex delivers unmatched protection and efficiency, keeping your engine running smoother for longer.</p>
      <svg class="seal" viewBox="0 0 44 44" role="img" aria-label="Engine certification seal"><use href="#seal"/></svg>
      <div class="volume"><span class="volume__number">4</span><span class="volume__unit">QUARTS</span></div>
    </div>
    <p class="variant__caption">4 Quarts</p>
  </section>

</main>
</body>
</html>
```